Wine Label Design-Crumbled Ledge Vineyard

Crumbled Ledge Vineyard is in the Barossa Valley in South Australia. The Barossa is recognized as Australia's premier wine region, producing Australia's icon wines and some " new takes on traditional".
This family owned and operated vineyard grows some exceptionally high quality fruit. Most of the fruit is sold and used for some of Australia's most iconic wines. Small quantities are retained by the owners for some wines with very limited availability. (Wines were previously sold as BrellMarston Vineyards Crumbled Ledge ( Shiraz, Cabernet etc).

The wines will in the future be labeled simply ‘Crumbled Ledge Vineyard’. The label will launch this new identity for the single family single vineyard and its high quality wines which are a true expression of the vineyard and derive from the Crumbled Ledge common to this ancient area (800-2000 million years old).
The label should reflect
• Single vineyard, family owned
• vines in very old rock & soils
• High quality & reliability
• Edgy but true, design based thinking (Please note:blue is generally seen as an unacceptable colour for a wine label?? Don’t ask me why)

The wines will be sold mostly direct in Australia ( ie not through retail stores), with limited export to Asia, Scandinavia and Canada.
There are three quality levels and price points in the portfolio
1. Entry level premium for everyday drinking for discriminating drinkers-approx AUD20
2. Super Premium-approx AUD30
3. Limited Release ultlra premium-AUD75-90?
We envisage three variations on the label but with an obvious & common design element. This design element should be able to be used for corporate identification and promotion
The paper stock will be waterproof and self adhesive. Our preference is for designs that engage the user by appealing to both sight and touch. It is preferred that textures be added eg embossing, high build varnish etc-rather than be a facet of the stock itself.
For information on statutory label requirements refer to www.vinoregistry-example.com . In brief
o Front label need not show any mandatory information. However we would prefer Variety, Barossa Valley, Year and alcohol to be shown on the front label
o Back label should show all mandatories and allow for a bar code

Reason: I've had a problem with my wireless broadband account and reception has been intermittent to say the least to the extent that I switched off at the weekend. Just going downtown now for a 'polite discussion' with my service provider.

Reason: I have receiver insufficient designs of quality which we would consider. Too many designs have a "cut and paste" appearance - too few exhibit an original art/design element which truly identifies the product.

Gals & Guys

most of the designs submitted lack punch and originality and are totally unmemorable.
Please-get on Zindle or whatever enter "Wine Label Designs" and do some research b4 u waste your time and mine. Formulaic cut and paste will not win the day. That's not to say that cut and paste can't work-but it must have some originality, impact and command attention. Please surprise me.

Following on from a question from a designer about who is our competition and what we are looking for I sent the following 
"I don't think I can add anything new. Read the brief and comments again and research wine labels on the web. In 30 minutes you'll get a good idea of the creative edgy designs in the industry. There are a plethora of collections. Our competition-anyone with a label. In 2010 there were over 2400 "producers" in other words 2400 producers with at least one label. In fact there are over 25000 Australian wines and then the numerous imported wines.

Target Market(s)

$20 people who budget everyday but have graduated from drinking 'entry level' wines. These people will likely fit into Cat. (b) in the $30 wine

$30 (a) will not over-compromise on some everyday discretionary expenditure.(b) might buy for special occasions

$70-$90 Professional/successful people with high disposable/discretionary income not particularly worried about recession. wine geeks.

Industry/Entity Type

Retail

Requirements
Must have
• identifiable element across range of wines

```html
<!DOCTYPE html>
<html lang="en">
<head>
<meta charset="utf-8">
<title>Crumbled Ledge Vineyard – Siraz Label</title>
<link rel="stylesheet" href="https://fonts.googleapis.com/css2?family=Crimson+Text&display=swap">
<style>
  :root {
    --backdrop: #111111;
    --label-wine: #800039;
    --text-white: #f6eef1;
    --varietal-gold: #a89868;
    --stones-light: rgba(246, 238, 241, 0.55);
    --stones-gold: rgba(190, 168, 120, 0.5);
  }
  html, body {
    margin: 0;
    padding: 0;
    width: 1200px;
    height: 900px;
    overflow: hidden;
    background: var(--backdrop);
  }
  .canvas {
    position: relative;
    width: 1200px;
    height: 900px;
  }
  .wine-label {
    position: absolute;
    left: 320px;
    top: 86px;
    width: 559px;
    height: 728px;
    font-family: "Crimson Text", "Minion Pro", Georgia, serif;
    color: var(--text-white);
  }
  .label-shape {
    position: absolute;
    inset: 0;
    width: 100%;
    height: 100%;
  }
  .label-shape path { fill: var(--label-wine); }
  .vineyard-name,
  .region,
  .varietal,
  .vintage,
  .alcohol {
    position: absolute;
    left: 31px;
    margin: 0;
    font-weight: 400;
    line-height: 1;
    white-space: nowrap;
  }
  .vineyard-name { top: 60px; font-size: 28px; left: 33px; }
  .region { top: 190px; font-size: 21px; left: 39px; }
  .stones-motif {
    position: absolute;
    left: 208px;
    top: 156px;
    width: 340px;
    height: 88px;
    border-radius: 44px;
    background: radial-gradient(ellipse at 55% 50%, var(--stones-light), var(--stones-gold) 60%, rgba(128, 0, 57, 0) 100%);
  }
  .varietal {
    top: 402px;
    font-size: 80px;
    color: var(--varietal-gold);
  }
  .vintage { top: 604px; font-size: 21px; }
  .alcohol { top: 640px; font-size: 21px; }
</style>
</head>
<body>
<main class="canvas">
  <section class="wine-label">
    <svg class="label-shape" viewBox="0 0 215 280" preserveAspectRatio="none" aria-hidden="true">
      <path d="M0 0 H190 C206 30 217 80 212 130 C207 180 182 224 142 247 C124 258 126 268 150 273 C180 278 205 276 215 280 V280 H0 Z"/>
    </svg>
    <h1 class="vineyard-name">Crumbled Ledge Vineyard</h1>
    <p class="region">Barossa Valley</p>
    <div class="stones-motif" role="img" aria-label="Line drawing of scattered rounded stones"></div>
    <h2 class="varietal">Siraz</h2>
    <p class="vintage">Year: 2012</p>
    <p class="alcohol">℮ 13.5% Alc.</p>
  </section>
</main>
</body>
</html>
```